Photographer Card

I'm currently doing freelance photography and i need a creative design name card especially when i attend events.
I require a design that makes a STATEMENT.
Simple, elegant and nothing like the usual name cards ive seen around (Example: with a camera/tripod etc in the design).

Photographer: Brent LW
Mobile: +65 91846257
E-mail: Brent.LW.Photography@mailvento.com
Facebook: www.friendspage.com/brent.lw.photography

Thanks for your time and hope it will turn out well! :)

Thanks for all your inputs!

Im liking the cursive feel.

Id prefer not to include the title "freelance"  :)

Also, im looking for a logo to establish myself

http://www.artnookgallery.com/art/Pebbles-Business-Card-506213847

Hi all! Thanks for the designs

"Capturing magical moments"
"Capturing magical moments that are gone forever"

Back design can be in big font "look HERE"

Maybe with focusing box 

Names can be played with horizontal and vertical.

Camera

Script

```html
<!DOCTYPE html>
<html lang="en">
<head>
<meta charset="utf-8">
<title>BLW Photography – Business Card</title>
<link rel="stylesheet" href="https://fonts.googleapis.com/css2?family=Delius&family=Michroma&family=Didact+Gothic&display=swap">
<style>
  :root {
    --ink: #000000;
    --paper: #ffffff;
    --frame: #5a5a5a;
    --quote: #f6a23e;
    --lime: #a9e233;
    --title: #e6e33a;
    --contact: #5fdde3;
    --cyan: #6ae0df;
    --green: #a3e02a;
    --yellow: #eccb1c;
    --orange: #e97813;
    --purple: #9257e0;
    --blue: #63b9f0;
    --lavender: #a48be6;
    --pink: #d9a7dd;
  }
  * { margin: 0; padding: 0; box-sizing: border-box; }
  html, body {
    width: 1097px; height: 1200px; overflow: hidden;
    background: var(--paper);
  }
  .canvas { position: relative; width: 1097px; height: 1200px; }
  .card {
    position: absolute; left: 4px; width: 1089px;
    background: var(--ink);
    border: 2px solid var(--frame);
    overflow: hidden;
  }
  .card--front { top: 4px; height: 579px; }
  .card--back { top: 613px; height: 574px; }

  .card__decor { position: absolute; inset: 0; width: 100%; height: 100%; }

  .colour-strip {
    position: absolute; left: 0; bottom: 0;
  }
  .card--front .colour-strip {
    width: 470px; height: 60px;
    background: linear-gradient(90deg, var(--yellow), var(--orange), var(--green), var(--cyan), var(--blue));
  }
  .card--back .colour-strip {
    width: 1008px; height: 76px;
    background: linear-gradient(90deg, var(--yellow), var(--orange), var(--green), var(--cyan), var(--blue), var(--lavender), var(--pink));
  }

  .tagline {
    position: absolute; left: 0; top: 98px; width: 640px;
    text-align: center;
    font-family: "Delius", cursive;
    font-size: 52px; line-height: 89px;
    color: var(--quote);
  }

  .brand { position: absolute; left: 0; top: 0; width: 780px; }
  .brand__name {
    position: absolute; left: 0; top: 34px; width: 780px;
    text-align: center;
    font-family: "Delius", cursive;
    font-size: 82px; line-height: 1;
    color: var(--lime);
    letter-spacing: 4px;
  }
  .brand__rule {
    position: absolute; left: 178px; top: 129px; width: 436px; height: 6px;
    background: var(--title);
  }
  .brand__title {
    position: absolute; left: 0; top: 168px; width: 780px;
    text-align: center;
    font-family: "Michroma", sans-serif;
    font-size: 42px; line-height: 1;
    color: var(--title);
    letter-spacing: 2px;
  }

  .contacts {
    position: absolute; left: 36px; top: 266px;
    list-style: none;
    font-family: "Didact Gothic", sans-serif;
    font-size: 36px; line-height: 52px;
    color: var(--contact);
  }
  .contacts li { display: flex; align-items: center; height: 52px; }
  .contacts svg { width: 44px; height: 40px; margin-right: 12px; flex: none; }
</style>
</head>
<body>
<div class="canvas">

  <section class="card card--front">
    <svg class="card__decor" viewBox="0 0 613 326" preserveAspectRatio="none" role="img" aria-label="Colourful diagonal band artwork">
      <defs>
        <linearGradient id="front-glow" x1="0" y1="0" x2="1" y2="0.4">
          <stop offset="0" stop-color="#6ae0df"/>
          <stop offset="0.4" stop-color="#a3e02a"/>
          <stop offset="0.7" stop-color="#eccb1c"/>
          <stop offset="1" stop-color="#e97813"/>
        </linearGradient>
      </defs>
      <polygon points="328,0 613,0 613,326 260,326 398,105" fill="url(#front-glow)"/>
    </svg>
    <div class="colour-strip" role="img" aria-label="Colour strip artwork"></div>
    <p class="tagline">"I'll Shoot you! ,<br>Its okay,<br>I'm a photographer"</p>
  </section>

  <section class="card card--back">
    <svg class="card__decor" viewBox="0 0 613 323" preserveAspectRatio="none" role="img" aria-label="Colourful diagonal band artwork">
      <defs>
        <linearGradient id="back-glow" x1="0" y1="0" x2="1" y2="0.4">
          <stop offset="0" stop-color="#6ae0df"/>
          <stop offset="0.45" stop-color="#a3e02a"/>
          <stop offset="0.75" stop-color="#eccb1c"/>
          <stop offset="1" stop-color="#e97813"/>
        </linearGradient>
      </defs>
      <polygon points="362,0 613,0 613,323 577,323" fill="url(#back-glow)"/>
    </svg>
    <div class="colour-strip" role="img" aria-label="Colour strip artwork"></div>

    <div class="brand">
      <p class="brand__name">BLW</p>
      <div class="brand__rule"></div>
      <p class="brand__title">PHOTOGRAPHY</p>
    </div>

    <ul class="contacts">
      <li>
        <svg viewBox="0 0 44 40" aria-hidden="true">
          <rect x="3" y="6" width="38" height="30" rx="4" fill="#d9dadb" stroke="#7a7a7a" stroke-width="2"/>
          <circle cx="22" cy="21" r="9" fill="#3a3a3a" stroke="#b0b0b0" stroke-width="2"/>
        </svg>
        : Brent LW
      </li>
      <li>
        <svg viewBox="0 0 44 40" aria-hidden="true">
          <rect x="13" y="2" width="18" height="36" rx="4" fill="#cfd6dc" stroke="#6a7078" stroke-width="2"/>
          <rect x="16" y="7" width="12" height="12" fill="#5fb2e6"/>
        </svg>
        : +65 91846257
      </li>
      <li>
        <svg viewBox="0 0 44 40" aria-hidden="true">
          <rect x="3" y="8" width="38" height="26" fill="#f2f2f2"/>
          <path d="M3,8 L22,24 L41,8" fill="none" stroke="#9a9a9a" stroke-width="2"/>
        </svg>
        : Brent.LW.Photography@mailvento.com
      </li>
      <li>
        <svg viewBox="0 0 44 40" aria-hidden="true">
          <rect x="6" y="3" width="34" height="34" fill="#3b5da8"/>
        </svg>
        : www.friendspage.com/brent.lw.photography
      </li>
    </ul>
  </section>

</div>
</body>
</html>
```